Stationary Design for Norvack Digital

We are after a full stationary back business cards, letterheads, compliment slip, invoice template, delivery note and anything else we could use within the stationary pack.

We would also like an email footer creating.

Our company details to be included on all stationary:

Registered Name: Norvack Limited
Company Registration Number: 20483957
Website: www.norvackdigital.example
email: info@norvackdigital.example
Phone: 01632 960 417
Address: 48 Elmstead Lane Loughborough Leicestershire United Kingdom LE14 7QW

Industry/Entity Type

Business

```html
<!DOCTYPE html>
<html lang="en">
<head>
<meta charset="utf-8">
<title>Norvack Digital – Stationery Pack</title>
<link rel="stylesheet" href="https://fonts.googleapis.com/css2?family=Open+Sans:wght@400;600;700&family=Arimo:wght@400;700&display=swap">
<style>
:root{
  --navy:#07306a;
  --blue:#1f3f8a;
  --grey-bar:#9c9ea4;
  --grey-line:#7d7f86;
  --stage:#b9b9b9;
  --paper:#ffffff;
  --mark:#e6e6e6;
  --ink:#222;
}
*{margin:0;padding:0;box-sizing:border-box}
html,body{width:1200px;height:1200px;overflow:hidden;background:var(--stage)}
body{position:relative;font-family:"Open Sans",Arial,sans-serif;color:var(--ink)}
.item{position:absolute;background:var(--paper);box-shadow:6px 8px 14px rgba(0,0,0,.28);overflow:hidden}
.brand{font-family:"Open Sans",Arial,sans-serif;font-weight:600;color:var(--blue);letter-spacing:.5px;white-space:nowrap;position:absolute}
.band{position:absolute;left:0;bottom:0;width:100%;display:block}
.abs{position:absolute}

/* business card */
.card-front{left:47px;top:62px;width:283px;height:186px}
.card-front .name{left:146px;top:24px;font-weight:700;font-size:10px;color:var(--navy)}
.card-front .role{left:146px;top:38px;font-size:8px}
.card-front .divider{left:136px;top:76px;width:1px;height:94px;background:var(--blue)}
.card-front .contacts{left:144px;top:77px;font-size:8.5px;color:#111;line-height:13px}
.card-front .contacts li{list-style:none;display:flex;align-items:center;gap:5px}
.card-front .contacts svg{width:7px;height:7px;fill:var(--navy)}
.card-front .addr{left:144px;top:134px;font-size:8.5px;color:var(--blue);line-height:11.5px}
.card-back{left:361px;top:62px;width:290px;height:191px;background:var(--navy)}
.card-back .brand{color:#fff;font-size:42px;left:0;right:0;top:70px;text-align:center}

/* compliment slip */
.slip{left:698px;top:62px;width:461px;height:230px}
.slip .title{right:26px;top:10px;font-size:14px;color:#3a56a0}

/* envelopes */
.env-a{left:93px;top:343px;width:500px;height:250px}
.env-a .divider{left:85px;top:13px;width:1px;height:28px;background:var(--blue)}
.env-a .addr{left:93px;top:18px;font-size:6px;line-height:8px;color:var(--blue)}
.env-b{left:634px;top:343px;width:500px;height:250px}

/* A4 sheets */
.sheet{width:366px;height:518px}
.letter{left:21px;top:638px}
.invoice{left:425px;top:634px}
.delivery{left:812px;top:638px}
.sheet .brand{left:39px;top:26px;font-size:22px}
.contact-block{left:254px;top:27px;font-size:4.6px;line-height:6.4px;color:#111;padding-left:6px;border-left:1px solid var(--blue)}
.contact-block .addr{color:var(--blue);margin-top:3px}
.watermark{position:absolute;left:0;right:0;text-align:center;font-weight:600;color:var(--mark);font-size:50px;letter-spacing:1px}

/* forms */
.form{font-family:Arimo,Arial,sans-serif;font-size:5.2px;color:#222}
.bar{position:absolute;background:var(--grey-bar);color:#fff;text-align:center;font-size:9px;line-height:12px;height:12px}
.lbl{position:absolute;font-size:5.2px}
table{border-collapse:collapse;position:absolute;table-layout:fixed;font-family:Arimo,Arial,sans-serif}
td,th{border:.6px solid var(--grey-line);font-size:4.8px;padding:0 2px;text-align:center;font-weight:700}
th{background:var(--grey-bar);color:#fff;height:8px}
.items th{background:#a7a9ae;color:#222}
.totals td{height:14px;background:#e4e4e6;text-align:left;padding-left:14px}
.totals td+td{background:#e4e4e6}
.info td{text-align:left;font-weight:400;height:7px}
.info th{text-align:left;background:#d9d9db;color:#222}
</style>
</head>
<body>

<!-- business card front -->
<section class="item card-front" aria-label="Business card front">
  <div class="abs name">Martin Ellery</div>
  <div class="abs role">Director</div>
  <div class="brand" style="left:18px;top:120px;font-size:26px">Norvack</div>
  <div class="abs divider"></div>
  <ul class="abs contacts">
    <li><svg viewBox="0 0 10 10"><rect x="2.5" y="0" width="5" height="10" rx="1"/></svg>1 555 014 2286</li>
    <li><svg viewBox="0 0 10 10"><path d="M2 0l2 2-1 2c1 1 2 2 3 3l2-1 2 2-2 2C4 10 0 6 0 2z"/></svg>01632 960 417</li>
    <li><svg viewBox="0 0 10 10"><path d="M0 2h10v7H0z M0 2l5 4 5-4" /></svg>info@norvackdigital.example</li>
    <li><svg viewBox="0 0 10 10"><circle cx="5" cy="5" r="5"/></svg>www.norvackdigital.example</li>
  </ul>
  <div class="abs addr">48 Elmstead Lane<br>Loughborough Leicestershire<br>United Kingdom LE14 7QW</div>
</section>

<!-- business card back -->
<section class="item card-back" aria-label="Business card back">
  <div class="brand">Norvack</div>
</section>

<!-- compliment slip -->
<section class="item slip" aria-label="Compliment slip">
  <div class="abs title">With Compliments</div>
  <svg class="band" viewBox="0 0 461 29" preserveAspectRatio="none" height="29">
    <polygon points="0,6 317,6 313,10 0,10" fill="#8a8c94"/>
    <polygon points="0,16 310,16 322,0 461,0 461,29 0,29" fill="var(--navy)"/>
  </svg>
</section>

<!-- envelope front -->
<section class="item env-a" aria-label="Envelope front">
  <div class="brand" style="left:16px;top:20px;font-size:16px">Norvack</div>
  <div class="abs divider"></div>
  <div class="abs addr">48 Elmstead Lane<br>Loughborough Leicestershire<br>United Kingdom LE14 7QW</div>
</section>

<!-- envelope back -->
<section class="item env-b" aria-label="Envelope back">
  <svg class="abs" style="left:0;top:0" width="500" height="80" viewBox="0 0 500 80">
    <path d="M1 0 L18 66 Q20 71 28 71 H475 Q482 71 484 66 L499 0" fill="none" stroke="#8a8fa8" stroke-width="1"/>
  </svg>
  <div class="brand" style="left:0;right:0;top:24px;font-size:20px;text-align:center">Norvack</div>
</section>

<!-- letterhead -->
<section class="item sheet letter" aria-label="Letterhead">
  <div class="brand">Norvack</div>
  <div class="abs contact-block">01632 960 417<br>info@norvackdigital.example<br>www.norvackdigital.example
    <div class="addr">48 Elmstead Lane<br>Loughborough Leicestershire<br>United Kingdom LE14 7QW</div></div>
  <div class="watermark" style="top:230px">Norvack</div>
  <svg class="band" viewBox="0 0 366 24" preserveAspectRatio="none" height="24">
    <polygon points="0,3 258,3 255,6 0,6" fill="#8a8c94"/>
    <polygon points="0,12 252,12 264,0 366,0 366,24 0,24" fill="var(--navy)"/>
  </svg>
</section>

<!-- invoice -->
<section class="item sheet invoice form" aria-label="Invoice template">
  <div class="brand">Norvack</div>
  <div class="abs contact-block">01632 960 417<br>info@norvackdigital.example<br>www.norvackdigital.example
    <div class="addr">48 Elmstead Lane<br>Loughborough Leicestershire<br>United Kingdom LE14 7QW</div></div>
  <div class="bar" style="left:38px;top:86px;width:291px">INVOICE</div>
  <div class="lbl" style="left:37px;top:106px">INVOICE TO:</div>
  <div class="lbl" style="left:37px;top:149px">SHIP TO:</div>
  <div class="lbl" style="left:218px;top:106px;line-height:10px">INVOICE #<br>INVOICE DATE<br>OUR ORDER NO.</div>
  <div class="lbl" style="left:268px;top:106px;line-height:10px">:<br>:<br>:</div>
  <div class="lbl" style="left:218px;top:144px;line-height:10px">TERMS<br>REP#<br>SHIPPED VIA<br>F.O.B.</div>
  <div class="lbl" style="left:268px;top:144px;line-height:10px">:<br>:<br>:<br>:</div>
  <div class="watermark" style="top:228px">Norvack</div>
  <table class="items" style="left:38px;top:188px;width:291px;height:166px">
    <colgroup><col style="width:22px"><col style="width:138px"><col style="width:37px"><col style="width:46px"><col style="width:48px"></colgroup>
    <tr><th>SL.</th><th>DESCRIPTION</th><th>QUANTITY</th><th>UNIT PRICE</th><th>AMOUNT</th></tr>
    <tr><td></td><td></td><td></td><td></td><td></td></tr>
  </table>
  <div class="lbl" style="left:38px;top:366px;font-weight:700">NOTES:</div>
  <div class="lbl" style="left:38px;top:376px;font-size:4.6px">* Payment terms are 100% pre-payment prior to shipment</div>
  <table class="totals" style="left:198px;top:355px;width:131px">
    <colgroup><col style="width:83px"><col style="width:48px"></colgroup>
    <tr><td>SUB TOTAL</td><td></td></tr>
    <tr><td>TAX RATE</td><td></td></tr>
    <tr><td>TAX</td><td></td></tr>
    <tr><td>FREIGHT</td><td></td></tr>
    <tr><td>GRAND TOTAL</td><td></td></tr>
  </table>
  <table class="info" style="left:36px;top:436px;width:94px">
    <tr><th>DIRECT ALL INQUIRIES TO:</th></tr>
    <tr><td>Name: xyz</td></tr>
    <tr><td>Phone: +00 12 345 6789</td></tr>
    <tr><td>Email: info@brightwellprint.example</td></tr>
  </table>
  <table class="info" style="left:137px;top:436px;width:193px">
    <tr><th colspan="2">WIRING INFORMATION:</th></tr>
    <tr><td colspan="2">xxxxxxxxxxx.cc</td></tr>
    <tr><td colspan="2">Bank Name</td></tr>
    <tr><td>Routing 026000000</td><td>Account 000029180000</td></tr>
  </table>
  <svg class="band" viewBox="0 0 366 24" preserveAspectRatio="none" height="24">
    <polygon points="0,3 258,3 255,6 0,6" fill="#8a8c94"/>
    <polygon points="0,12 252,12 264,0 366,0 366,24 0,24" fill="var(--navy)"/>
  </svg>
</section>

<!-- delivery note -->
<section class="item sheet delivery form" aria-label="Delivery note template">
  <div class="brand">Norvack</div>
  <div class="abs contact-block">01632 960 417<br>info@norvackdigital.example<br>www.norvackdigital.example
    <div class="addr">48 Elmstead Lane<br>Loughborough Leicestershire<br>United Kingdom LE14 7QW</div></div>
  <div class="bar" style="left:24px;top:86px;width:317px;font-weight:700">Delivery Note</div>
  <div class="lbl" style="left:211px;top:116px;line-height:9px">Order#:<br>Order date:</div>
  <div class="lbl" style="left:253px;top:116px;line-height:9px;font-weight:700">1234566<br>6-May-16</div>
  <div class="bar" style="left:25px;top:140px;width:98px;height:7px;font-size:5px;line-height:7px;text-align:left;padding-left:3px">BILL TO:</div>
  <div class="bar" style="left:210px;top:140px;width:131px;height:7px;font-size:5px;line-height:7px;text-align:left;padding-left:3px">SHIP TO:</div>
  <div class="lbl" style="left:26px;top:148px;line-height:8.5px"><b>[Company/ Name]</b><br>[Street Address]<br>[City, ST&nbsp; ZIP]<br>[Phone]</div>
  <div class="lbl" style="left:211px;top:148px;line-height:8.5px"><b>Lewis Hartley</b><br>[Street Address]<br>[City, ST&nbsp; ZIP]<br>[Phone]</div>
  <table style="left:25px;top:194px;width:316px">
    <colgroup><col style="width:58px"><col style="width:70px"><col style="width:99px"><col style="width:89px"></colgroup>
    <tr><th>ORDER DATE</th><th>ORDER #</th><th>PURCHASE ORDER #</th><th>CUSTOMER CONTACT</th></tr>
    <tr><td style="font-weight:400;height:9px">26-01-2010</td><td style="font-weight:400">[123456]</td><td style="font-weight:400">[123456]</td><td style="font-weight:400">Purchasing Dept.</td></tr>
  </table>
  <div class="watermark" style="top:224px">Norvack</div>
  <table style="left:25px;top:220px;width:316px">
    <colgroup><col style="width:58px"><col style="width:169px"><col style="width:45px"><col style="width:44px"></colgroup>
    <tr><th>ITEM #</th><th>DESCRIPTION</th><th>ORDER QTY</th><th>SHIP QTY</th></tr>
    <tr><td style="height:8px"></td><td></td><td style="font-weight:400">12</td><td style="font-weight:400">5</td></tr>
    <tr><td style="height:8px"></td><td></td><td style="font-weight:400">6</td><td style="font-weight:400">4</td></tr>
    <tr><td style="height:8px"></td><td></td><td></td><td></td></tr>
    <tr><td style="height:8px"></td><td></td><td></td><td></td></tr>
    <tr><td style="height:8px"></td><td></td><td></td><td></td></tr>
    <tr><td style="height:8px"></td><td></td><td></td><td></td></tr>
    <tr><td style="height:8px"></td><td></td><td></td><td></td></tr>
    <tr><td style="height:8px"></td><td></td><td></td><td></td></tr>
    <tr><td style="height:8px"></td><td></td><td></td><td></td></tr>
    <tr><td style="height:8px"></td><td></td><td></td><td></td></tr>
    <tr><td style="height:8px"></td><td></td><td></td><td></td></tr>
    <tr><td style="height:8px"></td><td></td><td></td><td></td></tr>
    <tr><td style="height:8px"></td><td></td><td></td><td></td></tr>
    <tr><td style="height:8px"></td><td></td><td></td><td></td></tr>
    <tr><td style="height:8px"></td><td></td><td></td><td></td></tr>
  </table>
  <div class="lbl" style="left:225px;top:355px;font-weight:700;font-size:6px">TOTAL:</div>
  <div class="lbl" style="left:252px;top:354px;width:45px;height:8px;background:#dcdcde;text-align:center;font-weight:700;font-size:6px">18</div>
  <div class="lbl" style="left:297px;top:354px;width:44px;height:8px;background:#dcdcde;text-align:center;font-weight:700;font-size:6px">9</div>
  <div class="abs" style="left:25px;top:371px;width:316px;height:44px;border:.6px solid var(--grey-line)">
    <div style="background:#c7c8cc;font-weight:700;font-size:5.2px;padding:1px 2px">COMMENTS:</div>
    <div style="font-size:5px;padding:1px 2px">Backordered items will ship as they become available. Etc</div>
  </div>
  <div class="lbl" style="left:0;right:0;top:426px;text-align:center;font-size:7.5px;color:#333">Thank You For Your Business!</div>
  <svg class="band" viewBox="0 0 366 24" preserveAspectRatio="none" height="24">
    <polygon points="0,3 258,3 255,6 0,6" fill="#8a8c94"/>
    <polygon points="0,12 252,12 264,0 366,0 366,24 0,24" fill="var(--navy)"/>
  </svg>
</section>

</body>
</html>
```